Modern Trendy Valentines Day Cards

Hi there! I found a design on Craftory that I want to replicate with a few changes. This should be very quick and straightforward.

I would like "Dane Morrow" crossed out on the card and on the side have Our Pixie Glamcousin written. Also please add my logo with the fairy somewhere.

These cards are going to my clients so I want to have a fun way of letting them know that I care about them and their business.

Target Market(s)

Ladies 25 - 40

Industry/Entity Type

Marketing

Requirements
Must have
• Cute and Whimsical design - trendy. Pop Culture.
Nice to have
• My logo - modern and cool font.
Should not have
• Boring, Simple colors.

```html
<!DOCTYPE html>
<html lang="en">
<head>
<meta charset="utf-8">
<title>Our Pixie Glamcousin – Valentine Card</title>
<link rel="stylesheet" href="https://fonts.googleapis.com/css2?family=Dancing+Script:wght@700&family=Luckiest+Guy&family=Emilys+Candy&display=swap">
<style>
  :root {
    --page: #ffffff;
    --frame: #ffffff;
    --frame-shadow: rgba(0, 0, 0, 0.18);
    --pink-edge: #e58c9a;
    --pink-mid: #edb3bb;
    --pink-glow: #f6dde0;
    --cloud: #f7dfe2;
    --brand-red: #e4224a;
    --balloon-red: #d8303c;
    --headline-red: #ea2a52;
    --headline-shade: #7d1a33;
    --list-pink: #e4589b;
    --box-pink: #e664a0;
    --box-side: #ffffff;
    --grass-dark: #7a1d16;
    --grass-light: #a22e24;
  }
  * { margin: 0; padding: 0; box-sizing: border-box; }
  html, body { width: 870px; height: 1200px; overflow: hidden; background: var(--page); }
  .canvas { position: relative; width: 870px; height: 1200px; }

  .frame {
    position: absolute; left: 47px; top: 50px; width: 748px; height: 1076px;
    background: var(--frame);
    box-shadow: 0 0 6px var(--frame-shadow);
  }
  .card {
    position: absolute; left: 90px; top: 87px; width: 661px; height: 1004px;
    overflow: hidden;
    background:
      radial-gradient(ellipse 55% 45% at 45% 50%, var(--pink-glow) 0%, rgba(246,221,224,0) 100%),
      radial-gradient(ellipse 80% 70% at 50% 45%, var(--pink-mid) 40%, var(--pink-edge) 100%);
  }

  .cloud { position: absolute; background: var(--cloud); border-radius: 30px 30px 6px 6px; opacity: 0.9; }
  .cloud--a { left: 374px; top: 44px; width: 66px; height: 30px; }
  .cloud--b { left: 33px; top: 278px; width: 60px; height: 26px; }
  .cloud--c { left: 554px; top: 278px; width: 74px; height: 32px; }
  .cloud--d { left: 56px; top: 546px; width: 72px; height: 34px; }

  .brand-mark {
    position: absolute; left: 52px; top: 40px; width: 250px; height: 250px;
    border-radius: 50%;
    background: radial-gradient(circle, rgba(228,34,74,0.35), rgba(228,34,74,0.12));
  }
  .balloon {
    position: absolute; left: 515px; top: 40px; width: 98px; height: 120px;
    border-radius: 46px 46px 18px 18px;
    background: linear-gradient(180deg, var(--balloon-red), #b51f2c);
  }

  .brand-name {
    position: absolute; font-family: 'Dancing Script', cursive; font-weight: 700;
    color: var(--brand-red); line-height: 1;
  }
  .brand-name__top { left: 338px; top: 140px; font-size: 44px; }
  .brand-name__main { left: 210px; top: 192px; font-size: 58px; }

  .headline {
    position: absolute; left: 216px; top: 272px;
    font-family: 'Luckiest Guy', sans-serif; font-size: 34px; letter-spacing: 1px;
    color: var(--headline-red);
    text-shadow: -2px 2px 0 var(--headline-shade);
  }

  .checklist { position: absolute; left: 273px; top: 362px; list-style: none; }
  .checklist__item {
    display: flex; align-items: center; height: 52px;
    font-family: 'Emilys Candy', cursive; font-size: 33px; color: var(--list-pink);
    -webkit-text-stroke: 0; paint-order: stroke fill;
    text-shadow: 2px 0 0 #fff, -2px 0 0 #fff, 0 2px 0 #fff, 0 -2px 0 #fff,
                 1px 1px 0 #fff, -1px -1px 0 #fff, 1px -1px 0 #fff, -1px 1px 0 #fff;
  }
  .checklist__box {
    flex: none; width: 21px; height: 21px; margin-right: 20px;
    background: var(--box-pink);
    box-shadow: 3px 3px 0 var(--box-side);
    position: relative;
  }
  .checklist__item--struck .checklist__label { text-decoration: line-through; text-decoration-thickness: 3px; }
  .checklist__box svg { position: absolute; left: -1px; top: -8px; }

  .credit {
    position: absolute; left: 273px; top: 842px;
    font-family: 'Emilys Candy', cursive; font-size: 24px; color: var(--list-pink);
    text-shadow: 1px 1px 0 #fff, -1px -1px 0 #fff, 1px -1px 0 #fff, -1px 1px 0 #fff;
  }
  .credit__name { text-decoration: line-through; text-decoration-thickness: 3px; }
  .credit__side { margin-left: 10px; color: var(--brand-red); font-family: 'Dancing Script', cursive; font-weight: 700; font-size: 28px; text-shadow: none; }

  .grass {
    position: absolute; left: 0; bottom: 0; width: 661px; height: 95px;
    background: linear-gradient(180deg, var(--grass-light) 0%, var(--grass-dark) 100%);
  }
</style>
</head>
<body>
<div class="canvas">
  <div class="frame"></div>
  <div class="card">
    <div class="cloud cloud--a"></div>
    <div class="cloud cloud--b"></div>
    <div class="cloud cloud--c"></div>
    <div class="cloud cloud--d"></div>

    <div class="brand-mark" role="img" aria-label="Brand emblem area: fairy silhouette with wings and wand"></div>
    <div class="balloon" role="img" aria-label="Illustration: red heart-shaped hot air balloon carrying a love letter"></div>

    <div class="brand-name brand-name__top">Our Pixie</div>
    <div class="brand-name brand-name__main">Glamcousin</div>

    <div class="headline">WRITTEN...</div>

    <ul class="checklist">
      <li class="checklist__item"><span class="checklist__box"></span><span class="checklist__label">give you up</span></li>
      <li class="checklist__item"><span class="checklist__box"></span><span class="checklist__label">let you down</span></li>
      <li class="checklist__item"><span class="checklist__box"></span><span class="checklist__label">run around</span></li>
      <li class="checklist__item"><span class="checklist__box"></span><span class="checklist__label">desert you</span></li>
      <li class="checklist__item"><span class="checklist__box"></span><span class="checklist__label">make you cry</span></li>
      <li class="checklist__item"><span class="checklist__box"></span><span class="checklist__label">say goodbye</span></li>
      <li class="checklist__item"><span class="checklist__box"></span><span class="checklist__label">tell a lie</span></li>
      <li class="checklist__item"><span class="checklist__box"></span><span class="checklist__label">hurt you</span></li>
      <li class="checklist__item"><span class="checklist__box">
        <svg width="30" height="30" viewBox="0 0 30 30" aria-hidden="true"><path d="M4 16 L11 23 L27 5" fill="none" stroke="#ffffff" stroke-width="3.5" stroke-linecap="round" stroke-linejoin="round"/></svg>
      </span><span class="checklist__label">all of the above</span></li>
    </ul>

    <div class="grass" role="img" aria-label="Illustration: dark red grass silhouette along the bottom edge"></div>
  </div>
</div>
</body>
</html>
```